Velorin Battery Saver App UI design.

We need a mockup layout design of an Velorin app uncoded. This simple battery saver app is composed primarily by three screens described in the attached specification. After the mockup approved we need the UI elements sliced, the app icon and a banner for the tuck market.

```html
<!DOCTYPE html>
<html lang="en">
<head>
<meta charset="utf-8">
<title>Velorin Battery Saver – Current Info</title>
<link href="https://fonts.googleapis.com/css2?family=Raleway:wght@300;400;600;700&family=Roboto:wght@400;500&display=swap" rel="stylesheet">
<style>
  :root {
    --stage-top: #4a6078;
    --stage-bottom: #1c2530;
    --screen-bg: #1f1f1f;
    --screen-bg-light: #2a2a2a;
    --brand-green: #3dbb76;
    --brand-green-dark: #2c9a5e;
    --tab-bg: #ffffff;
    --tab-muted: #3aa7cf;
    --ink: #ffffff;
    --ink-soft: #d8d8d8;
    --line: #cfcfcf;
    --ring: #22a6cf;
    --fill-blue: #3b95b4;
    --fill-blue-dark: #1c5b78;
  }
  * { box-sizing: border-box; margin: 0; padding: 0; }
  html, body { width: 1200px; height: 962px; overflow: hidden; }
  body {
    background: linear-gradient(160deg, var(--stage-top), var(--stage-bottom));
    font-family: "Raleway", sans-serif;
    color: var(--ink);
    position: relative;
  }
  .app-screen {
    position: absolute; left: 390px; top: 100px;
    width: 420px; height: 760px;
    background: linear-gradient(135deg, var(--screen-bg-light), var(--screen-bg));
    border-radius: 6px; overflow: hidden;
    box-shadow: 0 20px 60px rgba(0,0,0,.45);
  }
  .status-bar {
    height: 28px; background: var(--brand-green-dark);
    display: flex; justify-content: flex-end; align-items: center; gap: 6px;
    padding-right: 10px; font-family: "Roboto", sans-serif; font-size: 14px;
  }
  .app-bar {
    height: 56px; background: var(--brand-green);
    display: flex; align-items: center; gap: 12px; padding-left: 14px;
    font-size: 19px; font-weight: 400;
  }
  .app-mark { width: 28px; height: 28px; background: var(--ink); border-radius: 5px; }
  .tabs {
    height: 44px; background: var(--tab-bg);
    display: flex; font-size: 12px; font-weight: 600; color: var(--tab-muted);
  }
  .tab { flex: 1; text-align: center; line-height: 44px; white-space: nowrap; }
  .tab.is-active { color: var(--brand-green); border-bottom: 3px solid var(--brand-green); }
  .battery-gauge {
    position: absolute; left: 24px; top: 158px; width: 230px; height: 84px;
    border: 2px solid var(--line); border-radius: 6px;
  }
  .battery-gauge::after {
    content: ""; position: absolute; right: -12px; top: 24px;
    width: 10px; height: 32px; border: 2px solid var(--line); border-left: none; border-radius: 0 4px 4px 0;
  }
  .battery-fill {
    position: absolute; right: 4px; top: 4px; bottom: 4px; width: 60%;
    background: radial-gradient(circle at 60% 40%, var(--fill-blue), var(--fill-blue-dark));
    border-radius: 3px;
  }
  .battery-label {
    position: absolute; inset: 0; display: flex; align-items: center; justify-content: center; gap: 8px;
    font-size: 19px; font-weight: 300; letter-spacing: .5px;
  }
  .battery-label strong { font-weight: 700; }
  .state-label { position: absolute; left: 24px; top: 256px; font-size: 22px; font-weight: 700; letter-spacing: .5px; }
  .elapsed { position: absolute; left: 276px; top: 170px; display: flex; align-items: flex-start; gap: 5px; }
  .elapsed-unit { text-align: center; }
  .elapsed-box {
    width: 40px; height: 36px; background: #f4f4f4; color: #888; border-radius: 3px;
    font-size: 18px; line-height: 36px;
  }
  .elapsed-caption { font-size: 7px; letter-spacing: .5px; margin-top: 3px; }
  .elapsed-sep { font-size: 18px; line-height: 36px; }
  .elapsed-ago { font-size: 13px; font-weight: 700; line-height: 24px; }
  .save-button {
    position: absolute; left: 214px; top: 300px; width: 182px; height: 62px;
    background: var(--brand-green); border-radius: 6px;
    display: flex; align-items: center; gap: 10px; padding-left: 14px;
    font-size: 17px; font-weight: 600; white-space: nowrap;
    box-shadow: 0 0 14px rgba(61,187,118,.5);
  }
  .drain-ring { position: absolute; left: 24px; top: 318px; width: 160px; text-align: center; }
  .drain-ring svg { display: block; margin: 0 auto; }
  .drain-ring .ring-text {
    position: absolute; top: 38px; left: 0; right: 0; font-size: 17px; font-weight: 300; line-height: 1.2;
  }
  .drain-ring .ring-text b { font-weight: 700; }
  .drain-caption { font-size: 12px; margin-top: 10px; letter-spacing: .3px; }
  .menu { position: absolute; left: 24px; right: 24px; top: 470px; display: flex; flex-direction: column; gap: 10px; }
  .menu-item {
    height: 58px; border: 2px solid var(--line); border-radius: 5px;
    display: flex; align-items: center; gap: 22px; padding-left: 22px;
    font-size: 17px; font-weight: 400; color: var(--ink-soft);
  }
  .nav-bar {
    position: absolute; left: 0; right: 0; bottom: 0; height: 64px;
    display: flex; justify-content: space-around; align-items: center;
  }
</style>
</head>
<body>
  <main class="app-screen">
    <div class="status-bar">
      <svg width="16" height="12" viewBox="0 0 16 12"><path d="M8 12 0 3a12 12 0 0 1 16 0z" fill="#fff"/></svg>
      <svg width="12" height="12" viewBox="0 0 12 12"><path d="M12 0v12H0z" fill="#fff"/></svg>
      <svg width="8" height="13" viewBox="0 0 8 13"><rect x="0" y="1" width="8" height="12" rx="1" fill="#fff"/></svg>
      <span>12:06</span>
    </div>
    <header class="app-bar"><span class="app-mark"></span><span>Charge Keeper Plus!</span></header>
    <nav class="tabs">
      <span class="tab">HISTORY</span>
      <span class="tab is-active">CURRENT INFO</span>
      <span class="tab">POWER MANAGEMENT</span>
    </nav>

    <section class="battery-gauge">
      <div class="battery-fill" role="img" aria-label="Blue glowing battery charge fill"></div>
      <div class="battery-label"><strong>70%</strong> REMAINING</div>
    </section>
    <div class="elapsed">
      <div class="elapsed-unit"><div class="elapsed-box">03</div><div class="elapsed-caption">HOURS</div></div>
      <span class="elapsed-sep">:</span>
      <div class="elapsed-unit"><div class="elapsed-box">17</div><div class="elapsed-caption">MINUTES</div></div>
      <span class="elapsed-ago">AGO</span>
    </div>
    <div class="state-label">UNPLUGGED</div>

    <div class="save-button">
      <svg width="30" height="30" viewBox="0 0 30 30"><circle cx="15" cy="15" r="13" fill="none" stroke="#fff" stroke-width="2.5"/><path d="M16 5 10 16h5l-1 9 6-11h-5z" fill="#fff"/></svg>
      SAVE BATTERY
    </div>

    <div class="drain-ring">
      <svg width="120" height="120" viewBox="0 0 120 120"><circle cx="60" cy="60" r="54" fill="none" stroke="var(--ring)" stroke-width="5"/></svg>
      <div class="ring-text"><b>1</b> Day<br><b>19</b> Hours</div>
      <div class="drain-caption">UNTIL DRAINED</div>
    </div>

    <div class="menu">
      <div class="menu-item">
        <svg width="36" height="28" viewBox="0 0 36 28"><polyline points="3,24 10,6 20,20 33,4" fill="none" stroke="var(--brand-green)" stroke-width="2"/><g fill="#fff"><circle cx="3" cy="24" r="2.5"/><circle cx="10" cy="6" r="2.5"/><circle cx="20" cy="20" r="2.5"/><circle cx="33" cy="4" r="2.5"/></g></svg>
        View Battery Use
      </div>
      <div class="menu-item">
        <svg width="36" height="28" viewBox="0 0 36 28"><path d="M13 2v7M23 2v7" stroke="#fff" stroke-width="3"/><path d="M9 9h18v5a9 9 0 0 1-18 0z" fill="#fff"/><path d="M18 23v5" stroke="var(--brand-green)" stroke-width="3"/></svg>
        Power Management
      </div>
      <div class="menu-item">
        <svg width="36" height="28" viewBox="0 0 36 28"><circle cx="12" cy="12" r="7" fill="none" stroke="#fff" stroke-width="4" stroke-dasharray="3 2.5"/><circle cx="26" cy="20" r="5" fill="none" stroke="var(--brand-green)" stroke-width="3" stroke-dasharray="2.5 2"/></svg>
        Settings
      </div>
    </div>

    <nav class="nav-bar">
      <svg width="32" height="22" viewBox="0 0 32 22"><path d="M28 18h-14a7 7 0 0 1 0-14h14M10 0 4 4l6 4" fill="none" stroke="#fff" stroke-width="2"/></svg>
      <svg width="34" height="22" viewBox="0 0 34 22"><path d="M3 21V10L17 2l14 8v11z" fill="none" stroke="#fff" stroke-width="2"/></svg>
      <svg width="30" height="22" viewBox="0 0 30 22"><rect x="2" y="7" width="22" height="14" fill="none" stroke="#fff" stroke-width="2"/><path d="M6 3h21v13" fill="none" stroke="#fff" stroke-width="2"/></svg>
    </nav>
  </main>
</body>
</html>
```